Presentation Folder, Business Card, Letterhead and Envelope design

We are a dental clinic that will open in August and we are looking for a professional graphic designer to create our Business Card, Presentation Folder, Letterhead, Notepad and envelopes.

The brand NovaGrin must reflect a sense of quality and sophistication, marketed for middle-class consumers.
Our preference is for quality and refined materials, where less is more.
Attached the logo

```html
<!DOCTYPE html>
<html lang="en">
<head>
<meta charset="utf-8">
<title>NovaGrin Business Card</title>
<link rel="stylesheet" href="https://fonts.googleapis.com/css2?family=Work+Sans:wght@300;400;600&display=swap">
<style>
  :root {
    --backdrop: #ece8e4;
    --card-frost: #f4f3f2;
    --card-edge: #dcd8d4;
    --brand-red: #7a0c0e;
    --brand-red-deep: #5e0709;
    --name-gold: #e0c3a6;
    --panel-text: #f3e6e3;
    --logo-ink: #3c3c3e;
  }
  * { margin: 0; padding: 0; box-sizing: border-box; }
  html, body {
    width: 1200px;
    height: 887px;
    overflow: hidden;
    background: var(--backdrop);
    font-family: "Work Sans", Arial, sans-serif;
  }
  .business-card {
    position: absolute;
    left: 150px;
    top: 196px;
    width: 900px;
    height: 494px;
    border-radius: 22px;
    background: var(--card-frost);
    border: 1px solid var(--card-edge);
    box-shadow: 0 18px 40px rgba(60, 40, 30, 0.18);
    overflow: hidden;
  }
  .brand-lockup {
    position: absolute;
    left: 48px;
    top: 224px;
    display: flex;
    align-items: center;
    gap: 14px;
  }
  .brand-square {
    width: 44px;
    height: 44px;
    background: var(--brand-red);
  }
  .brand-name {
    font-weight: 300;
    font-size: 42px;
    letter-spacing: 0.22em;
    color: var(--logo-ink);
    line-height: 1;
  }
  .contact-panel {
    position: absolute;
    left: 454px;
    top: 0;
    width: 446px;
    height: 100%;
    background: linear-gradient(100deg, var(--brand-red) 0%, var(--brand-red-deep) 100%);
    color: var(--panel-text);
  }
  .panel-notch {
    position: absolute;
    left: -1px;
    top: 124px;
    width: 26px;
    height: 48px;
    background: var(--card-frost);
    clip-path: polygon(0 0, 100% 50%, 0 100%);
  }
  .holder-name {
    position: absolute;
    left: 55px;
    top: 116px;
    font-weight: 600;
    font-size: 30px;
    letter-spacing: 0.02em;
    color: var(--name-gold);
    line-height: 1;
  }
  .holder-title {
    position: absolute;
    left: 55px;
    top: 152px;
    font-weight: 400;
    font-size: 21px;
    color: var(--name-gold);
  }
  .postal-address {
    position: absolute;
    left: 55px;
    top: 226px;
    font-style: normal;
    font-size: 21px;
    line-height: 29px;
  }
  .contact-list {
    position: absolute;
    left: 55px;
    top: 314px;
    list-style: none;
    font-size: 21px;
    line-height: 29px;
  }
  .contact-list li {
    display: flex;
    align-items: center;
    gap: 10px;
  }
  .contact-icon {
    width: 15px;
    height: 15px;
    flex: none;
  }
</style>
</head>
<body>
  <main class="business-card">
    <div class="brand-lockup">
      <span class="brand-square"></span>
      <span class="brand-name">NOVAGRIN</span>
    </div>

    <section class="contact-panel">
      <span class="panel-notch"></span>
      <h1 class="holder-name">DANIEL HARLOW</h1>
      <p class="holder-title">Director</p>
      <address class="postal-address">
        418 Willow Crest Road<br>
        Brookfield, MO 64628
      </address>
      <ul class="contact-list">
        <li>
          <svg class="contact-icon" viewBox="0 0 16 16" aria-hidden="true">
            <path d="M4 1.5 L6.2 4.3 L5 6 C5.8 7.8 7.6 9.8 9.8 11 L11.4 9.7 L14.3 11.8 L13 14.3 C7.6 14 2.3 8.6 1.8 3 Z" fill="none" stroke="currentColor" stroke-width="1.3" stroke-linejoin="round"/>
          </svg>
          <span>+330 5172-3046</span>
        </li>
        <li>
          <svg class="contact-icon" viewBox="0 0 16 16" aria-hidden="true">
            <rect x="1.5" y="3.5" width="13" height="9" fill="none" stroke="currentColor" stroke-width="1.3"/>
            <path d="M1.5 3.5 L8 9 L14.5 3.5" fill="none" stroke="currentColor" stroke-width="1.3"/>
          </svg>
          <span>hello@novagrin.com</span>
        </li>
        <li>
          <svg class="contact-icon" viewBox="0 0 16 16" aria-hidden="true">
            <circle cx="8" cy="8" r="6.5" fill="none" stroke="currentColor" stroke-width="1.2"/>
            <ellipse cx="8" cy="8" rx="3" ry="6.5" fill="none" stroke="currentColor" stroke-width="1.1"/>
            <path d="M1.5 8 H14.5 M2.6 4.6 H13.4 M2.6 11.4 H13.4" stroke="currentColor" stroke-width="1.1"/>
          </svg>
          <span>www.novagrin.com</span>
        </li>
      </ul>
    </section>
  </main>
</body>
</html>
```